Design of an attractive membership brochure/membership card for an Electrical Business

Hi, we are an electrical business based in Sydney, Australia.

Our design's aim is to attract and target new customers into using our business as a repeat for anything electrical in their home. We would be handing this out to them after a job is completed and they're happy with the service.
We're thinking of a brochure, possibly additional membership cards with personalized number ID's for each client.

Open to ideas, but some of the things we want to include on our brochure are perks of why the client should sign up with us as a lifetime client
- Discounted emergency call out fees outside of normal hours
- Lifetime membership price, one time payment
- Exclusive 10% member discount on all future jobs
- Priority on any during business hour jobs or emergencies

If any other questions please don't hesitate to reach out.
We've attached our logo for reference for the mock designs.
Our website
https://brightwirecrew.com.au/

```html
<!DOCTYPE html>
<html lang="en">
<head>
<meta charset="utf-8">
<title>Bright Wire Crew – Membership Card and Brochure</title>
<link rel="stylesheet" href="https://fonts.googleapis.com/css2?family=Open+Sans:ital,wght@0,300;0,400;0,600;0,700;0,800;1,400;1,600;1,700;1,800&display=swap">
<style>
:root{
  --stage:#d4d4d4;
  --ink:#262626;
  --ink-deep:#141414;
  --red:#d4311f;
  --red-deep:#a8231a;
  --white:#ffffff;
  --field:#e6e6e6;
  --grey:#9a9a9a;
}
*{margin:0;padding:0;box-sizing:border-box}
html,body{width:1200px;height:2173px;overflow:hidden}
body{background:var(--stage);position:relative;font-family:"Open Sans",Arial,sans-serif;color:var(--white)}
.piece{position:absolute;overflow:hidden;box-shadow:0 6px 10px rgba(0,0,0,.25)}

/* membership card */
.card{top:86px;width:510px;height:321px;background:var(--ink-deep)}
.card--front{left:75px}
.card--back{left:615px}
.card__photo{position:absolute;inset:0;background:radial-gradient(circle at 72% 55%,#3b3632 0%,#1e1c1b 35%,#121212 70%)}
.brand{position:absolute;display:flex;align-items:center;gap:6px;font-weight:700;white-space:nowrap}
.brand__dot{width:8px;height:8px;background:var(--red)}
.card .brand{top:42px;right:37px;font-size:13px;color:var(--white)}
.field{position:absolute;background:var(--field);border-radius:3px}
.label{position:absolute;font-weight:300;font-size:19px;letter-spacing:-.3px}
.card__title{position:absolute;left:36px;top:140px;font-size:28px;font-weight:600;letter-spacing:-.3px}
.card__title span{color:var(--red)}
.card__site{position:absolute;right:37px;top:262px;font-size:13px;font-weight:300;color:#c9c9c9}
.card__benefits{position:absolute;left:37px;top:65px;font-size:12px;line-height:17px;font-weight:400}
.card__benefits h3{font-size:14px;font-weight:400;color:var(--red);margin-bottom:4px}
.card__contacts{position:absolute;right:37px;top:234px;text-align:right;font-size:12px;line-height:17px}
.card__contacts li{list-style:none;display:flex;justify-content:flex-end;align-items:center;gap:7px}
.card__contacts .phone{font-weight:700;font-size:13px}
.ico{width:12px;height:12px;flex:none}

/* brochure */
.brochure{left:59px;width:1082px;height:770px}
.brochure--outside{top:465px}
.brochure--inside{top:1310px}
.panel{position:absolute;top:0;height:770px;overflow:hidden}
.panel--left{left:0;width:539px}
.panel--right{left:539px;width:543px}
.panel--light{background:var(--white);color:var(--ink)}
.panel--dark{background:var(--ink)}

.cover-deco{position:absolute;left:0;top:0}
.cover-brand{top:58px;left:85px;font-size:36px;color:var(--ink)}
.cover-brand .brand__dot{width:14px;height:14px}
.bubble{position:absolute;left:72px;background:var(--ink);border:2px solid #111;border-radius:22px;color:var(--white);font-style:italic;box-shadow:0 3px 6px rgba(0,0,0,.3)}
.bubble--signup{top:310px;width:362px;height:154px;padding:16px 16px 0 17px;font-size:24px;line-height:29px;font-weight:600}
.bubble--join{top:577px;width:360px;height:87px;padding:6px 12px 0 15px;font-size:24px;line-height:30px;font-weight:600}
.accent{color:var(--red);font-weight:800}
.bubble--signup .accent{font-size:29px}
.bubble--join .accent{font-size:33px;display:block;line-height:34px}

.hero-photo{position:absolute;left:0;top:0}
.headline{position:absolute;left:27px;top:582px;font-size:39px;line-height:39px;font-weight:800;font-style:italic;letter-spacing:.3px;text-transform:uppercase}
.headline .lead{color:var(--red)}
.headline-bar{position:absolute;left:425px;top:668px;width:118px;height:26px}

.panel--about{background:linear-gradient(180deg,#232323 0%,#2b2b2b 55%,#3a3a3a 100%)}
.room-photo{position:absolute;left:0;top:430px;width:539px;height:340px;background:radial-gradient(ellipse at 55% 40%,#9b9b9b 0%,#5a5a5a 40%,#2a2a2a 80%)}
.pill{position:absolute;background:var(--red);border-radius:16px;color:var(--white);font-weight:800;font-style:italic;text-transform:uppercase;box-shadow:0 3px 5px rgba(0,0,0,.25)}
.pill--about{left:22px;top:63px;width:302px;height:88px;padding:6px 0 0 23px;font-size:29px;line-height:36px;border:2px solid #e85b49}
.pill--about .gap{display:inline-block;width:75px;height:15px;background:#2b2b2b;border-radius:4px;vertical-align:middle;margin-left:4px}
.about-text{position:absolute;left:22px;top:197px;width:450px;font-size:14.6px;line-height:18.2px;font-weight:400;color:#eee}
.about-text p+p{margin-top:18px}
.about-contact{position:absolute;left:22px;top:600px;font-style:italic;font-size:17px;line-height:20px}
.about-contact strong{font-weight:800}
.call-btn{display:inline-block;margin-top:4px;background:var(--red);border-radius:5px;padding:0 10px;font-size:17px;line-height:23px;font-weight:600}

.pill--benefits{left:36px;top:63px;width:457px;height:65px;font-size:29px;line-height:61px;text-align:center;border:2px solid #e85b49}
.benefits-sub{position:absolute;left:54px;top:140px;font-size:17px;font-style:italic;font-weight:600;color:var(--ink)}
.benefits{position:absolute;left:34px;top:207px;list-style:none}
.benefits li{display:flex;gap:25px;height:63px;align-items:flex-start}
.benefit-icon{width:47px;height:47px;background:var(--red);border-radius:3px;flex:none;display:flex;align-items:center;justify-content:center}
.benefit-icon svg{width:30px;height:30px}
.benefits p{width:370px;font-size:17px;line-height:19.5px;font-style:italic;font-weight:600;color:var(--ink);padding-top:6px}
.pill--info{left:225px;top:588px;width:203px;height:42px;font-size:19px;line-height:42px;text-align:center;border-radius:10px;font-weight:800}
.info-list{position:absolute;left:236px;top:646px;list-style:none;color:var(--ink);font-size:18.5px;font-style:italic;font-weight:600}
.info-list li{display:flex;align-items:center;gap:12px;height:28px}
.info-list .ico{width:16px;height:16px}
</style>
</head>
<body>

<!-- Membership card, front -->
<section class="piece card card--front">
  <div class="card__photo" role="img" aria-label="Dark background photo of hanging vintage light bulbs"></div>
  <div class="brand"><span class="brand__dot"></span>Bright Wire Crew</div>
  <div class="field" style="left:38px;top:37px;width:260px;height:32px"></div>
  <div class="label" style="left:37px;top:69px">NAME</div>
  <h1 class="card__title">MEMBERSHIP <span>CARD</span></h1>
  <div class="field" style="left:38px;top:202px;width:188px;height:31px"></div>
  <div class="field" style="left:235px;top:202px;width:89px;height:31px"></div>
  <div class="label" style="left:37px;top:233px">MEMBERSHIP ID</div>
  <div class="label" style="left:234px;top:233px">SINCE</div>
  <div class="card__site">www.brightwirecrew.com.au</div>
</section>

<!-- Membership card, back -->
<section class="piece card card--back">
  <div class="card__photo" role="img" aria-label="Dark background photo of hanging vintage light bulbs"></div>
  <div class="brand"><span class="brand__dot"></span>Bright Wire Crew</div>
  <div class="card__benefits">
    <h3>BENEFITS OF LIFETIME MEMBERSHIP</h3>
    <p>Discounted emergency call out fees</p>
    <p>A lifetime membership price</p>
    <p>Exclusive discounts</p>
    <p>Priority service</p>
  </div>
  <div class="label" style="left:37px;top:222px;font-size:15px">MEMBER'S SIGNATURE</div>
  <div class="field" style="left:37px;top:246px;width:151px;height:37px"></div>
  <ul class="card__contacts">
    <li class="phone"><svg class="ico" viewBox="0 0 24 24"><path fill="#d4311f" d="M6.6 10.8a15 15 0 0 0 6.6 6.6l2.2-2.2c.3-.3.7-.4 1-.2 1.1.4 2.3.6 3.6.6.6 0 1 .4 1 1V20c0 .6-.4 1-1 1A17 17 0 0 1 3 4c0-.6.4-1 1-1h3.5c.6 0 1 .4 1 1 0 1.3.2 2.5.6 3.6.1.3 0 .7-.2 1z"/></svg>0400 555 019</li>
    <li><svg class="ico" viewBox="0 0 24 24"><circle cx="12" cy="12" r="9" fill="none" stroke="#d4311f" stroke-width="2.5"/></svg>brightwirecrew_au</li>
    <li><svg class="ico" viewBox="0 0 24 24"><path fill="#d4311f" d="M2 5h20v14H2z"/><path fill="none" stroke="#141414" stroke-width="1.6" d="M2 5l10 8 10-8"/></svg>services@brightwirecrew.com.au</li>
  </ul>
</section>

<!-- Brochure, outside spread -->
<section class="piece brochure brochure--outside">
  <div class="panel panel--left panel--light">
    <svg class="cover-deco" width="539" height="770" viewBox="0 0 539 770" aria-hidden="true">
      <polygon points="0,77 34,77 24,103 0,103" fill="#262626"/>
      <polygon points="40,77 70,77 60,103 30,103" fill="#d4311f"/>
      <rect x="0" y="309" width="61" height="152" rx="12" fill="#9a9a9a" opacity=".7"/>
      <circle cx="-10" cy="275" r="125" fill="none" stroke="#d4311f" stroke-width="60"/>
      <circle cx="-10" cy="275" r="82" fill="none" stroke="#a8231a" stroke-width="12"/>
      <rect x="0" y="577" width="61" height="86" rx="12" fill="#9a9a9a" opacity=".7"/>
      <circle cx="-5" cy="708" r="112" fill="none" stroke="#d4311f" stroke-width="54"/>
      <circle cx="-5" cy="708" r="76" fill="none" stroke="#a8231a" stroke-width="12"/>
    </svg>
    <div class="brand cover-brand"><span class="brand__dot"></span>Bright Wire Crew</div>
    <p class="bubble bubble--signup">Sign up for our lifetime <span class="accent">membership</span> and enjoy exclusive perks and peace of <span class="accent">mind</span></p>
    <p class="bubble bubble--join">Join our family of satisfied <span class="accent">customers today!</span></p>
  </div>
  <div class="panel panel--right panel--dark">
    <svg class="hero-photo" width="543" height="770" viewBox="0 0 543 770">
      <defs>
        <radialGradient id="heroTone" cx="50%" cy="45%" r="60%">
          <stop offset="0" stop-color="#c8634a"/>
          <stop offset=".45" stop-color="#4a5a86"/>
          <stop offset="1" stop-color="#1b1b1b"/>
        </radialGradient>
      </defs>
      <circle cx="278" cy="268" r="228" fill="url(#heroTone)" role="img" aria-label="Photo of a smiling electrician in an orange hard hat and blue overalls holding a clipboard"/>
      <circle cx="278" cy="268" r="231" fill="none" stroke="#d4311f" stroke-width="6"/>
      <path d="M0 452 C70 395 150 390 230 470 C300 540 420 520 543 450 L543 770 L0 770 Z" fill="#262626"/>
      <path d="M0 452 C70 395 150 390 230 470 C300 540 420 520 543 450" fill="none" stroke="#d4311f" stroke-width="8"/>
    </svg>
    <h2 class="headline"><span class="lead">Experience</span><br>The electrician you<br>can trust for life</h2>
    <svg class="headline-bar" viewBox="0 0 118 26" aria-hidden="true">
      <polygon points="8,0 96,0 88,26 0,26" fill="#d4311f"/>
      <polygon points="102,0 118,0 118,26 94,26" fill="#ffffff"/>
    </svg>
  </div>
</section>

<!-- Brochure, inside spread -->
<section class="piece brochure brochure--inside">
  <div class="panel panel--left panel--about">
    <div class="room-photo" role="img" aria-label="Photo of a crystal chandelier hanging in a grey room"></div>
    <h2 class="pill pill--about">About us -<span class="gap"></span><br>Bright Wire Crew</h2>
    <div class="about-text">
      <p>Bright Wire Crew is a Sydney-based electrical business specialising in electrical maintenance work for residential, commercial, strata and real estate clients. It began with two mates with a strong desire to change the image of tradies and provide exceptional service. As a team of electricians based in the Inner West of Sydney, we understand the need of everyday people struggling to find good, reliable and trustworthy electricians.</p>
      <p>At Bright Wire Crew, we have high expectations of ourselves and strive to improve every day. We’re always available around the clock to provide professional advice or give a helping hand when in need.</p>
    </div>
    <div class="about-contact">
      Get In Contact Today<br>
      <strong>0400 555 019</strong><br>
      <span class="call-btn">CALL NOW</span>
    </div>
  </div>
  <div class="panel panel--right panel--light">
    <h2 class="pill pill--benefits">Benefits of membership:</h2>
    <p class="benefits-sub">A detailed list of the benefits of lifetime membership</p>
    <ul class="benefits">
      <li><span class="benefit-icon"><svg viewBox="0 0 24 24"><path fill="none" stroke="#fff" stroke-width="1.6" d="M6.6 10.8a15 15 0 0 0 6.6 6.6l2.2-2.2 4.6 1.6V20A17 17 0 0 1 3 4h3.5l1.6 4.6z"/><circle cx="17" cy="7" r="5" fill="none" stroke="#fff" stroke-width="1.4"/></svg></span><p>Discounted emergency call out fees outside of normal hours</p></li>
      <li><span class="benefit-icon"><svg viewBox="0 0 24 24"><circle cx="12" cy="12" r="10" fill="none" stroke="#fff" stroke-width="1.4"/><rect x="8" y="6" width="8" height="12" fill="none" stroke="#fff" stroke-width="1.4"/><path stroke="#fff" stroke-width="1.2" d="M10 9h4M10 12h4M10 15h4"/></svg></span><p>Lifetime membership price, one-time payment</p></li>
      <li><span class="benefit-icon"><svg viewBox="0 0 24 24"><path fill="none" stroke="#fff" stroke-width="1.5" d="M3 13l9-9h8v8l-9 9z"/><circle cx="16" cy="8" r="1.5" fill="#fff"/></svg></span><p>Exclusive 10% member discount on all future jobs</p></li>
      <li><span class="benefit-icon"><svg viewBox="0 0 24 24"><path fill="none" stroke="#fff" stroke-width="1.4" d="M9 4h12v4H9zM9 10h12v4H9zM9 16h12v4H9zM5 4v16M3 18l2 2 2-2"/></svg></span><p>Priority on any during business hour jobs or emergencies</p></li>
    </ul>
    <div class="pill pill--info">For more info</div>
    <ul class="info-list">
      <li><svg class="ico" viewBox="0 0 24 24"><path fill="#d4311f" d="M6.6 10.8a15 15 0 0 0 6.6 6.6l2.2-2.2c.3-.3.7-.4 1-.2 1.1.4 2.3.6 3.6.6.6 0 1 .4 1 1V20c0 .6-.4 1-1 1A17 17 0 0 1 3 4c0-.6.4-1 1-1h3.5c.6 0 1 .4 1 1 0 1.3.2 2.5.6 3.6.1.3 0 .7-.2 1z"/></svg>0400 555 019</li>
      <li><svg class="ico" viewBox="0 0 24 24"><path fill="#d4311f" d="M2 5h20v14H2z"/><path fill="none" stroke="#fff" stroke-width="1.6" d="M2 5l10 8 10-8"/></svg>services@brightwirecrew.com.au</li>
      <li><svg class="ico" viewBox="0 0 24 24"><circle cx="12" cy="12" r="9" fill="none" stroke="#d4311f" stroke-width="2.5"/></svg>brightwirecrew_au</li>
      <li><svg class="ico" viewBox="0 0 24 24"><g fill="none" stroke="#d4311f" stroke-width="1.8"><circle cx="12" cy="12" r="10"/><ellipse cx="12" cy="12" rx="4.5" ry="10"/><path d="M2 12h20M4 7h16M4 17h16"/></g></svg>www.brightwirecrew.com.au</li>
    </ul>
  </div>
</section>

</body>
</html>
```